New web design for a service provider in the medical field

We are looking for a new design for our website. We are a company that repairs and sells medical endoscopes. Our customers include doctors and hospitals. Our current website can be found at https://lumenfix.example/en/lumenfix-english.
We need a new web design (without programming) for the following 3 pages:
-Startpage https://lumenfix.example/en/lumenfix-english/
-Used endoscopes https://lumenfix.example/en/used-endoscopes/
-Purchase https://lumenfix.example/en/purchase/
The design should be modern and stylish.
The blue color of the logo should be reflected on the page, but not too intrusive.
I have uploaded the images from the header. If more images are needed, let me know and I will upload them.

Target Market(s)
Doctors and hospitals

```html
<!DOCTYPE html>
<html lang="en">
<head>
<meta charset="utf-8">
<title>LumenFix – Endoscope Repair</title>
<link rel="stylesheet" href="https://fonts.googleapis.com/css2?family=Poppins:wght@400;500;600;700;800&display=swap">
<style>
:root{
  --blue:#2a8fd8;
  --blue-light:#3aa0e6;
  --navy:#1b2d4a;
  --deep:#0f3c9c;
  --band:#0d5cc4;
  --pale:#eaf3fb;
  --line:#3f78c4;
  --text:#3a4658;
  --white:#ffffff;
}
*{margin:0;padding:0;box-sizing:border-box}
html,body{width:1200px;height:4118px;overflow:hidden}
body{font-family:'Poppins',sans-serif;color:var(--text);background:var(--white);position:relative}
.abs{position:absolute}
a{color:inherit;text-decoration:none}

/* header */
.topbar{left:715px;top:0;width:485px;height:38px;background:var(--pale);display:flex;align-items:center;gap:28px;padding-left:32px;font-size:12px;color:var(--navy)}
.topbar span{display:flex;align-items:center;gap:8px}
.topbar b{font-weight:600}
.logo{left:128px;top:28px;font-size:22px;font-weight:700;color:var(--navy);display:flex;align-items:center;gap:8px}
.logo i{width:12px;height:12px;border-radius:50%;background:var(--blue);display:block}
.nav{top:62px;left:315px;display:flex;gap:34px;font-size:12px;font-weight:700;color:var(--navy);letter-spacing:.1px}
.nav .active{color:var(--blue)}

/* hero */
.hero{left:0;top:98px;width:1200px;height:600px;background:linear-gradient(100deg,#8a9aab 0%,#5c7594 35%,#486c9e 60%,#2f5fa8 80%,#7c8fa4 100%)}
.hero h1{left:122px;top:185px;font-size:34px;line-height:46px;font-weight:800;color:var(--white);text-transform:uppercase}
.hero p{left:126px;top:283px;font-size:14px;line-height:24px;color:#eef3f9;width:420px}
.btn{display:flex;align-items:center;justify-content:center;border-radius:30px;font-weight:600;color:var(--white);text-transform:uppercase}
.hero .btn{left:124px;top:343px;width:192px;height:52px;background:var(--blue);font-size:15px}
.arrow{width:44px;height:44px;border-radius:50%;background:rgba(255,255,255,.85);display:flex;align-items:center;justify-content:center}
.hero-wave{left:0;top:600px;width:1200px;height:130px}

/* intro */
.intro-photo{left:122px;top:824px;width:448px;height:448px;border-radius:50%;background:radial-gradient(circle at 45% 40%,#6f757c 0%,#3b4046 45%,#9ba2a8 100%)}
.intro-ring{left:106px;top:806px;width:480px;height:240px}
.intro h2{left:612px;top:825px;font-size:27px;line-height:37px;font-weight:700;color:var(--navy);text-transform:uppercase}
.intro h2 span{font-weight:400}
.intro p{left:615px;width:450px;font-size:14px;line-height:24px}
.intro .btn{left:612px;top:1177px;width:166px;height:47px;background:var(--blue);font-size:14px}

/* service cards */
.svc{top:1382px;width:325px;height:268px;border:2px solid var(--line);border-radius:4px;text-align:center;padding:52px 26px 0}
.svc h3{font-size:15px;font-weight:600;color:var(--navy);margin-bottom:12px}
.svc p{font-size:11.5px;line-height:21px;height:110px}
.svc .btn{margin:0 auto;width:134px;height:36px;background:var(--deep);font-size:11px;position:absolute;left:50%;transform:translateX(-50%);bottom:25px}
.svc-icon{top:-42px;left:50%;margin-left:-41px;width:82px;height:82px;border-radius:50%;background:var(--blue);display:flex;align-items:center;justify-content:center}

/* faulty band */
.band{left:0;top:1737px;width:1200px;height:420px;background:radial-gradient(ellipse at 55% 30%,#3d8ef0 0%,#1565d4 45%,#0a4fb7 100%)}
.band h2{left:0;width:1200px;top:1832px;text-align:center;color:var(--white);font-size:28px;font-weight:700}
.band p{left:0;width:1200px;top:1870px;text-align:center;color:var(--white);font-size:28px;font-weight:400}
.band .btn{left:512px;top:1936px;width:170px;height:50px;border:2px solid var(--white);font-size:14px}

/* outcome */
.outcome{left:0;top:2140px;width:1200px;height:540px;background:var(--pale)}
.outcome h2{left:110px;top:2200px;font-size:30px;line-height:37px;font-weight:800;color:var(--navy)}
.oc{top:2315px;width:264px;height:190px;border:2px solid #b6d2ea;border-radius:4px;background:var(--pale);padding:64px 0 0 32px}
.oc.first{background:var(--white);border-color:#9cc3e6;box-shadow:0 6px 18px rgba(30,80,140,.15)}
.oc h3{font-size:16px;line-height:19px;font-weight:500;color:var(--navy);margin-bottom:6px}
.oc p{font-size:11px;line-height:17px;color:#6a7587;width:220px}
.oc svg{position:absolute;left:34px;top:16px}
.dots{top:2530px;left:555px;display:flex;gap:10px}
.dots i{width:40px;height:3px;background:#86b7e4;display:block}
.dots i:first-child{background:var(--blue)}

/* decision */
.decision h2{left:0;width:1200px;top:2706px;text-align:center;font-size:28px;line-height:37px;font-weight:700;color:var(--navy);text-transform:uppercase}
.dc{width:314px;height:215px;border:2px solid #8ab7e0;border-radius:4px;text-align:center;padding:0 36px;display:flex;flex-direction:column;align-items:center}
.dc svg{margin:34px 0 10px}
.dc h3{font-size:17px;line-height:18px;font-weight:600;color:var(--navy);margin-bottom:10px}
.dc p{font-size:10.5px;line-height:15px}
.dc.on{background:var(--blue);border-color:var(--blue);color:var(--white)}
.dc.on h3{color:var(--white)}

/* contact */
.contact{left:0;top:3355px;width:1200px;height:540px;background:linear-gradient(135deg,#1f5fc2 0%,#0f47b0 55%,#0a3e9f 100%)}
.contact h2{left:0;width:1200px;top:3426px;text-align:center;color:var(--white);font-size:28px;font-weight:700}
.field{border:1px solid rgba(255,255,255,.55);color:var(--white);font-size:12px;padding:14px 18px 0}
.contact .btn{left:532px;top:3734px;width:162px;height:44px;background:var(--blue-light);font-size:13px}
.foot-wave{left:0;top:3840px;width:1200px;height:90px}
.foot-logo{left:0;width:1200px;top:3882px;text-align:center;font-size:21px;font-weight:700;color:var(--navy)}
.foot-nav{left:0;width:1200px;top:3985px;display:flex;justify-content:center;gap:42px;font-size:13px;font-weight:700;color:var(--navy)}
.copy{left:0;width:1200px;top:4026px;text-align:center;font-size:12px;color:var(--navy)}
.social{left:560px;top:4060px;display:flex;gap:8px}
.social i{width:32px;height:32px;border:2px solid var(--blue);border-radius:50%;display:block}
</style>
</head>
<body>

<header>
  <div class="abs topbar">
    <span><svg width="18" height="13" viewBox="0 0 18 13" fill="none" stroke="#2a8fd8" stroke-width="1.4"><rect x="1" y="1" width="16" height="11"/><path d="M1 1l8 6 8-6"/></svg>info@lumenfix.example</span>
    <span><svg width="14" height="14" viewBox="0 0 14 14" fill="none" stroke="#2a8fd8" stroke-width="1.4"><path d="M3 1l2.5 3L4 6c1 2 2 3 4 4l2-1.5L13 11l-1.5 2C6 13 1 8 1 2.5z"/></svg><b>+49 4000 555 010-0</b></span>
  </div>
  <div class="abs logo"><i></i>LumenFix</div>
  <nav class="abs nav">
    <a class="active" href="https://lumenfix.example/en/lumenfix-english/">ENDOSCOPE REPAIR</a>
    <a href="https://lumenfix.example/en/used-endoscopes/">USED ENDOSCOPES</a>
    <a href="#">ENDOSCOPY SYSTEMS</a>
    <a href="#">ENDOSCOPY ACCESSORIES</a>
    <a href="https://lumenfix.example/en/purchase/">PURCHASE</a>
  </nav>
</header>

<section>
  <div class="abs hero" role="img" aria-label="Technician in blue gloves holding an endoscope control section in a clinic"></div>
  <h1 class="abs hero" style="background:none;height:auto;width:auto;left:122px;top:283px;font-size:34px;line-height:46px;font-weight:800;color:#fff">PUT YOUR ENDOSCOPE IN<br>RELIABLE HANDS!</h1>
  <p class="abs" style="left:126px;top:380px;font-size:14px;line-height:24px;color:#eef3f9;width:420px">Lorem ipsum dolor sit amet, consectetur adipiscing elit, sed do eiusmod tempor incididunt ut labore.</p>
  <a class="abs btn" href="#" style="left:124px;top:441px;width:192px;height:52px;background:var(--blue);font-size:15px">LEARN MORE</a>
  <div class="abs arrow" style="left:26px;top:342px"><svg width="12" height="16" viewBox="0 0 12 16" fill="none" stroke="#1b2d4a" stroke-width="2"><path d="M9 2L3 8l6 6"/></svg></div>
  <div class="abs arrow" style="left:1116px;top:342px"><svg width="12" height="16" viewBox="0 0 12 16" fill="none" stroke="#1b2d4a" stroke-width="2"><path d="M3 2l6 6-6 6"/></svg></div>
  <svg class="abs hero-wave" viewBox="0 0 1200 130" preserveAspectRatio="none">
    <path d="M0 60 C300 20 600 0 900 20 C1050 30 1150 25 1200 10 L1200 130 L0 130Z" fill="#2a8fd8"/>
    <path d="M0 72 C300 36 600 18 900 36 C1050 46 1150 40 1200 28 L1200 130 L0 130Z" fill="#ffffff"/>
  </svg>
</section>

<section class="intro">
  <div class="abs intro-photo" role="img" aria-label="Close-up of an endoscope control head with angulation knobs"></div>
  <svg class="abs intro-ring" viewBox="0 0 480 240" fill="none"><path d="M4 236 A236 236 0 0 1 476 236" stroke="#0f3c9c" stroke-width="4"/></svg>
  <h2 class="abs">Endoscope repairs and<br>second hand endoscopes<br><span>from LumenFix –<br>cause the outcome matters!</span></h2>
  <p class="abs" style="top:984px">LumenFix is a privileged partner for the start-up facility or optimisation of existing healthcare facilities, doctor's offices and hospitals. The quality and reliability of our products and our offered service are our best advertisement!</p>
  <p class="abs" style="top:1104px">As a result of optimised processes and highly qualified specialists in our company, we can work very quickly</p>
  <a class="abs btn" href="#">LEARN MORE</a>
</section>

<section>
  <div class="abs svc" style="left:115px">
    <div class="abs svc-icon"><svg width="44" height="44" viewBox="0 0 44 44" fill="none" stroke="#fff" stroke-width="2.4" stroke-linecap="round"><path d="M8 8l28 28M36 8L8 36M6 12l6-6M32 38l6-6"/></svg></div>
    <h3>Endoscope repair service</h3>
    <p>Manufacturer-independent we repair and maintain endoscopes, individual components (e.g. processors or light sources), accessories and peripherals of the manufacturers Orvane, Pelmar and Kasumi.</p>
    <a class="btn" href="#">REPAIR REQUEST</a>
  </div>
  <div class="abs svc" style="left:451px">
    <div class="abs svc-icon"><svg width="40" height="48" viewBox="0 0 40 48" fill="none" stroke="#fff" stroke-width="2.4"><path d="M12 46V20a8 8 0 0 1 16 0v26M8 20a12 12 0 0 1 24 0"/><circle cx="20" cy="20" r="3"/></svg></div>
    <h3>Sale Used endoscopes</h3>
    <p>Our regular stock includes refurbished gastroscopes, coloscopes, bronchoscopes, cystoscopes and duodenoscopes from the well-known manufacturers Orvane, Pelmar and Kasumi.</p>
    <a class="btn" href="https://lumenfix.example/en/used-endoscopes/">PURCHASE REQUEST</a>
  </div>
  <div class="abs svc" style="left:787px">
    <div class="abs svc-icon"><svg width="44" height="44" viewBox="0 0 44 44" fill="none" stroke="#fff" stroke-width="2.4"><rect x="6" y="10" width="22" height="28"/><path d="M14 24l8 8 14-20"/></svg></div>
    <h3>Purchase Used endoscopes</h3>
    <p>We are very interested in buying your old endoscopes – even defective and dismantled! We offer fair conditions! Please contact us for a purchase offer!</p>
    <a class="btn" href="https://lumenfix.example/en/purchase/">SELL DEVICE</a>
  </div>
</section>

<section>
  <div class="abs band" role="img" aria-label="Blue backdrop with a hand and soft light particles"></div>
  <h2 class="abs" style="left:0;width:1200px;top:1832px;text-align:center;color:#fff;font-size:28px;font-weight:700">FAULTY EV?</h2>
  <p class="abs" style="left:0;width:1200px;top:1870px;text-align:center;color:#fff;font-size:28px">We ensure quick and smooth repairs! Simple place</p>
  <a class="abs btn" href="#" style="left:512px;top:1936px;width:170px;height:50px;border:2px solid #fff;font-size:14px">PICK UP ORDER</a>
</section>

<section>
  <div class="abs outcome"></div>
  <svg class="abs" style="left:0;top:2090px" width="1200" height="70" viewBox="0 0 1200 70" preserveAspectRatio="none"><path d="M0 70 C250 20 600 40 850 20 C1000 8 1120 4 1200 0 L1200 70Z" fill="#eaf3fb"/></svg>
  <h2 class="abs" style="left:110px;top:2200px;font-size:30px;line-height:37px;font-weight:800;color:var(--navy)">CAUSE THE<br>OUTCOME MATTERS!</h2>
  <div class="abs oc first" style="left:106px"><svg width="46" height="44" viewBox="0 0 46 44" fill="none" stroke="#1b2d4a" stroke-width="1.6"><circle cx="23" cy="10" r="6"/><circle cx="9" cy="22" r="5"/><circle cx="37" cy="22" r="5"/><path d="M13 42c0-8 4-14 10-14s10 6 10 14M1 40c0-6 3-10 8-10M45 40c0-6-3-10-8-10"/></svg><h3>One company for<br>everyone</h3><p>We are a service provider for doctors and hospitals!</p></div>
  <div class="abs oc" style="left:389px"><svg width="40" height="44" viewBox="0 0 40 44" fill="none" stroke="#1b2d4a" stroke-width="1.6"><rect x="6" y="2" width="28" height="38"/><circle cx="20" cy="16" r="6"/><path d="M16 22l-2 10 6-3 6 3-2-10"/></svg><h3>Experience<br>charactorises us</h3><p>Our team has many years of experience in the business field!</p></div>
  <div class="abs oc" style="left:674px"><svg width="40" height="44" viewBox="0 0 40 44" fill="none" stroke="#1b2d4a" stroke-width="1.6"><path d="M6 42V14a10 10 0 0 1 20 0"/><rect x="18" y="22" width="18" height="18"/></svg><h3>The product is close<br>to our hearts</h3><p>We repair and sell second hand, flexible endoscopes!</p></div>
  <div class="abs oc" style="left:955px;width:264px"><svg width="40" height="44" viewBox="0 0 40 44" fill="none" stroke="#1b2d4a" stroke-width="1.6"><path d="M20 2l16 6v12c0 12-8 19-16 22C12 39 4 32 4 20V8z"/><path d="M13 22l5 5 9-10"/></svg><h3>Guaranteed<br>service</h3><p>You receive a six-month warranty on all repairs!</p></div>
  <div class="abs dots"><i></i><i></i><i></i></div>
  <svg class="abs" style="left:0;top:2640px" width="1200" height="50" viewBox="0 0 1200 50" preserveAspectRatio="none"><path d="M0 30 C200 0 350 10 600 25 C850 40 1050 35 1200 20 L1200 50 L0 50Z" fill="#ffffff"/></svg>
</section>

<section class="decision">
  <h2 class="abs">LumenFix GmbH, your decision<br>for your future</h2>
  <div class="abs dc on" style="left:118px;top:2816px"><svg width="48" height="48" viewBox="0 0 44 44" fill="none" stroke="#fff" stroke-width="2" stroke-linecap="round"><path d="M8 8l28 28M36 8L8 36M6 12l6-6M32 38l6-6"/></svg><h3>Fast repairs</h3><p>Keep potential disruptions in your doctor's office or in your hospital at minimum as a result of optimized processes and highly qualified specialists</p></div>
  <div class="abs dc" style="left:454px;top:2816px"><svg width="48" height="48" viewBox="0 0 48 48" fill="none" stroke="#2a8fd8" stroke-width="1.6"><circle cx="12" cy="10" r="7"/><path d="M8 46V32h6v14M20 46V24h6v22M32 46V16h6v30M44 46V6"/></svg><h3>Highly cost efficient</h3><p>Benefit from our first class recommendations and implementation by our experienced staff. Our goals is to find the best solutions together with you at the best lowest price point.</p></div>
  <div class="abs dc" style="left:795px;top:2816px"><svg width="64" height="44" viewBox="0 0 64 44" fill="none" stroke="#2a8fd8" stroke-width="1.6"><path d="M14 6h30v24H14zM44 14h10l6 8v8H44"/><circle cx="22" cy="34" r="5"/><circle cx="50" cy="34" r="5"/><path d="M2 14h8M4 20h8M6 26h6"/></svg><h3>On-site service</h3><p>We will gladly pay you a visit to to carry out analysis and repairs on site. Due to our many years of experience – it doesn't get any faster (whiglelthin a 250 km range)</p></div>
  <div class="abs dc" style="left:118px;top:3050px"><svg width="48" height="48" viewBox="0 0 48 48" fill="none" stroke="#2a8fd8" stroke-width="1.6"><rect x="14" y="4" width="26" height="30"/><circle cx="27" cy="19" r="7"/><path d="M2 44l10-10h14M2 34h8"/></svg><h3>Loan equipment service</h3><p>Use our service of high-quality loan devices during the downtime of your defective endoscope (limited to stock</p></div>
  <div class="abs dc" style="left:454px;top:3050px"><svg width="44" height="48" viewBox="0 0 44 48" fill="none" stroke="#2a8fd8" stroke-width="1.6"><path d="M6 2h22l8 8v24H6zM12 14h16M12 20h16M12 26h10"/><path d="M20 44l8-8 8 4 6-6"/></svg><h3>Without a maintenance<br>contract</h3><p>No subscription or other maintenance contract, but one-time and sustainable repair work</p></div>
  <div class="abs dc" style="left:795px;top:3050px"><svg width="56" height="48" viewBox="0 0 56 48" fill="none" stroke="#2a8fd8" stroke-width="1.6"><path d="M20 6v14M28 2v14M36 6v14M4 20c8 0 12 12 24 12s16-12 24-12M14 44h28M28 32v12"/></svg><h3>First class service</h3><p>Our clients always come first!</p></div>
</section>

<section>
  <div class="abs contact"></div>
  <h2 class="abs" style="left:0;width:1200px;top:3426px;text-align:center;color:#fff;font-size:28px;font-weight:700">HOW CAN WE HELP YOU</h2>
  <div class="abs field" style="left:274px;top:3493px;width:332px;height:44px">First Name</div>
  <div class="abs field" style="left:619px;top:3493px;width:331px;height:44px">Last Name</div>
  <div class="abs field" style="left:274px;top:3549px;width:332px;height:44px">Email address</div>
  <div class="abs field" style="left:619px;top:3549px;width:331px;height:44px">Phone</div>
  <div class="abs field" style="left:274px;top:3605px;width:676px;height:107px">Message</div>
  <a class="abs btn" href="#" style="left:532px;top:3734px;width:162px;height:44px;background:var(--blue-light);font-size:13px">SUBMIT NOW</a>
  <svg class="abs foot-wave" viewBox="0 0 1200 90" preserveAspectRatio="none">
    <path d="M0 30 C300 50 460 10 600 4 C760 10 900 50 1200 30 L1200 90 L0 90Z" fill="#2a8fd8"/>
    <path d="M0 40 C300 58 470 18 600 14 C750 18 900 58 1200 40 L1200 90 L0 90Z" fill="#ffffff"/>
  </svg>
</section>

<footer>
  <div class="abs foot-logo">LumenFix</div>
  <nav class="abs foot-nav">
    <a href="https://lumenfix.example/en/lumenfix-english/">ENDOSCOPE REPAIR</a>
    <a href="https://lumenfix.example/en/used-endoscopes/">USED ENDOSCOPES</a>
    <a href="#">ENDOSCOPY SYSTEMS</a>
    <a href="#">ENDOSCOPY ACCESSORIES</a>
    <a href="https://lumenfix.example/en/purchase/">PURCHASE</a>
  </nav>
  <div class="abs copy">© 2022 LumenFix GmbH | Privacy Policy | Information</div>
  <div class="abs social"><i></i><i></i><i></i></div>
</footer>

</body>
</html>
```